Rooted Ready Rising: Quiet Roots, Open Doors, Steady Hands

I want a modern and clean looking book cover. 5.25x8

Title
Rooted Ready Rising

Subtitle
Quiet Roots, Open Doors, Steady Hands

I don’t just want a graphic, I want it to make sense. If it can just be the words and a textured looking background, I’ll be ok with that too. I just want it to look crisp, clean, modern.

I want the back to have my book blurb and bio attached with the pic that’s attached.

Target Market(s)

Self help

Requirements
Must have
• Modern, clean look, look professional, attract customers.

```html
<!DOCTYPE html>
<html lang="en">
<head>
<meta charset="utf-8">
<title>Rooted Ready Rising – Book Cover</title>
<link rel="stylesheet" href="https://fonts.googleapis.com/css2?family=Oswald:wght@300;400;600&family=Roboto+Condensed:wght@300;400&display=swap">
<style>
  :root {
    --ink-dark: #2b2c31;
    --crimson: #8c1a2c;
    --crimson-deep: #6a1220;
    --crimson-glow: #a8283d;
    --paper: #ffffff;
  }
  * { margin: 0; padding: 0; box-sizing: border-box; }
  html, body { width: 1200px; height: 914px; overflow: hidden; background: var(--ink-dark); }
  .cover { position: relative; width: 1200px; height: 914px; overflow: hidden; color: var(--paper); }

  .cover-art {
    position: absolute; inset: 0;
    background:
      radial-gradient(ellipse 420px 260px at 910px 470px, rgba(200,70,90,.55), transparent 70%),
      linear-gradient(180deg, var(--ink-dark) 0%, #2f2b33 34%, #6e1828 46%, var(--crimson-glow) 56%, var(--crimson) 74%, var(--crimson-deep) 100%);
  }
  .back-top-band {
    position: absolute; left: 0; top: 0; width: 628px; height: 416px;
    background: var(--ink-dark);
  }
  .back-bottom-band {
    position: absolute; left: 0; top: 416px; width: 628px; height: 498px;
    background: linear-gradient(180deg, rgba(140,26,44,.92), rgba(106,18,32,.85));
  }

  /* Back cover */
  .back { position: absolute; left: 0; top: 0; width: 580px; height: 914px; font-family: 'Oswald', sans-serif; }
  .back-title { position: absolute; left: 31px; top: 24px; font-size: 40px; font-weight: 600; line-height: 1.1; letter-spacing: .2px; }
  .back-subtitle { position: absolute; left: 33px; top: 70px; font-size: 17px; font-weight: 300; }
  .blurb { position: absolute; left: 33px; top: 100px; width: 520px; font-weight: 300; font-size: 12.6px; line-height: 17px; }
  .blurb .hook { font-size: 15px; font-weight: 600; margin-bottom: 9px; }
  .blurb p { margin-bottom: 9px; }
  .blurb strong { font-weight: 600; }

  .author-photo {
    position: absolute; left: 33px; top: 446px; width: 126px; height: 124px;
    background: linear-gradient(180deg, #d9d9d9, #bfbfbf);
  }
  .bio { position: absolute; left: 33px; top: 446px; width: 520px; font-weight: 300; font-size: 12.6px; line-height: 17px; }
  .bio .wrap-beside { margin-left: 133px; }
  .bio p { margin-bottom: 8px; }
  .bio strong { font-weight: 600; }
  .bio .gap { margin-top: 16px; }

  .isbn-box { position: absolute; left: 322px; top: 740px; width: 228px; height: 136px; background: var(--paper); }

  /* Spine */
  .spine { position: absolute; left: 575px; top: 0; width: 53px; height: 914px; font-family: 'Roboto Condensed', sans-serif; font-weight: 300; }
  .spine-title, .spine-author {
    position: absolute; left: 0; width: 53px; writing-mode: vertical-rl;
    text-transform: uppercase; white-space: nowrap; line-height: 53px; text-align: left;
  }
  .spine-title { top: 30px; font-size: 47px; }
  .spine-author { top: 610px; font-size: 33px; }

  /* Front cover */
  .front { position: absolute; left: 628px; top: 0; width: 572px; height: 914px; font-family: 'Roboto Condensed', sans-serif; font-weight: 300; text-align: center; }
  .front-author { position: absolute; left: 0; right: 0; top: 36px; font-size: 46px; text-transform: uppercase; }
  .front-title { position: absolute; left: 0; right: 0; top: 334px; font-size: 56px; text-transform: uppercase; white-space: nowrap; }
  .front-subtitle { position: absolute; left: 0; right: 0; top: 422px; font-size: 22px; font-weight: 400; text-transform: uppercase; letter-spacing: .3px; }
</style>
</head>
<body>
<main class="cover">
  <div class="cover-art" role="img" aria-label="Photograph of a person standing on a mountain peak with arms raised against a red sky and clouds"></div>
  <div class="back-top-band"></div>
  <div class="back-bottom-band"></div>

  <section class="back">
    <h2 class="back-title">ROOTED READY RISING</h2>
    <p class="back-subtitle">Quiet Roots, Open Doors, Steady Hands</p>
    <div class="blurb">
      <p class="hook">Everyone has big dreams and lofty goals, but few give themselves permission to try.</p>
      <p><strong>Rooted Ready Rising</strong>: Quiet Roots, Open Doors, Steady Hands is for anyone who has ever been stymied by negative self-talk, maltreatment, troubles at home, relationship problems, or has experienced anything significant that has made you want to abandon your dreams.</p>
      <p>Part memoir, part self-help book, part spiritual guide, this book aims to provide encouragement and a helping hand to anyone who feels like life has passed them by or think their time will never come.</p>
      <p>Inside, you’ll find deeply personal stories and anecdotes from Author Delia Hartwell. Her personal experiences provide a detailed account and roadmap for how to lift yourself out of a dark spot, find your voice, dream bigger, dare to try, and change your life for the better.</p>
      <p>If you’ve ever felt like where you are now is where you’ll always be or fear that your prayers will never be answered, this book will help you move past obstacles, shatter expectations, and learn how to confidently bet on yourself because you’re worth it.</p>
      <p>Scroll up and click “Buy now” to find the support and motivation you need to move forward in life and finally be who you were meant to be!</p>
    </div>

    <div class="author-photo" role="img" aria-label="Author portrait photo"></div>
    <div class="bio">
      <p class="wrap-beside"><strong>Delia Hartwell</strong> is a helper. For as long as she can remember, she’s always wanted to do the right thing, but life, circumstance, and some very tough years, set her on a path that conflicted with what was in her heart… until something clicked and she made herself and her goals a priority.</p>
      <p class="wrap-beside">A dreamer and visionary at her core, she knows all too well how much faith and courage it takes to defy expectations and build your own path forward. Her tenacity led her in a direction that would change her life for the better.</p>
      <p>After being told she wasn’t “college material” in high school, she made it her mission to never allow anyone to define who she is, and more importantly, to empower others to do the same. Today, the devout Christian, Author, Motivator, Coach, Educator, and Educational Leader, holds 3 degrees (Bachelors of Science in Psychology, Master of Education, and Educational Specialist) and is currently in the dissertation phase of a Doctorate of Education. Recently, she added Life Coach to her resume.</p>
      <p class="gap">When she’s not teaching, studying, coaching, reading, writing, listening to music, or helping others achieve their goals, she spends as much time as she can with her loving husband, three beautiful daughters, her college aged God-daughter, and countless friends.</p>
    </div>
    <div class="isbn-box"></div>
  </section>

  <section class="spine">
    <span class="spine-title">Rooted Ready Rising</span>
    <span class="spine-author">Delia Hartwell</span>
  </section>

  <section class="front">
    <p class="front-author">Delia Hartwell</p>
    <h1 class="front-title">Rooted Ready Rising</h1>
    <p class="front-subtitle">Quiet Roots, Open Doors, Steady Hands</p>
  </section>
</main>
</body>
</html>
```